Leonard Vasto Card

My father, Leonard Vasto, just retired at 69 years old and he needs a new business/social card that looks professional and includes some sort of logo - perhaps his initials LV. It needs to include his phone number and email address and that's it. So fairly limited text but still elegant.

Industry/Entity Type

Business

```html
<!DOCTYPE html>
<html lang="en">
<head>
<meta charset="utf-8">
<title>Leonard Vasto — Business Card</title>
<link rel="stylesheet" href="https://fonts.googleapis.com/css2?family=Roboto:wght@300&display=swap">
<style>
  :root {
    --page-bg: #e4e4e6;
    --card-bg: #ffffff;
    --band-grey: #6e6e6e;
    --ink-grey: #6a6a6a;
    --band-text: #ececec;
    --band-text-soft: #d6d6d6;
  }
  html, body {
    margin: 0;
    width: 1200px;
    height: 900px;
    overflow: hidden;
    background: var(--page-bg);
    font-family: "Roboto", "Helvetica Neue", Arial, sans-serif;
    font-weight: 300;
  }
  .business-card {
    position: absolute;
    left: 100px;
    top: 185px;
    width: 1000px;
    height: 530px;
    background: var(--card-bg);
    overflow: hidden;
  }
  .contact-band {
    position: absolute;
    left: 0;
    right: 0;
    bottom: 0;
    height: 191px;
    background: var(--band-grey);
  }
  .monogram {
    position: absolute;
    left: 72px;
    bottom: 191px;
    margin: 0;
    font-size: 380px;
    line-height: 0.74;
    letter-spacing: -18px;
    color: var(--band-grey);
    font-weight: 300;
  }
  .holder-name {
    position: absolute;
    left: 508px;
    bottom: 197px;
    margin: 0;
    font-size: 40px;
    line-height: 1;
    color: var(--ink-grey);
    font-weight: 300;
  }
  .contact-list {
    position: absolute;
    left: 508px;
    top: 22px;
    margin: 0;
    padding: 0;
    list-style: none;
  }
  .contact-phone {
    font-size: 38px;
    line-height: 1.1;
    color: var(--band-text);
  }
  .contact-email {
    font-size: 24px;
    line-height: 1.3;
    color: var(--band-text-soft);
  }
</style>
</head>
<body>
  <main class="business-card">
    <p class="monogram">LV</p>
    <h1 class="holder-name">Leonard Vasto</h1>
    <section class="contact-band">
      <ul class="contact-list">
        <li class="contact-phone">00 0000000</li>
        <li class="contact-email">email@website.com</li>
      </ul>
    </section>
  </main>
</body>
</html>
```